Ashgrove Orthopaedic logo and letterhead

Letterhead AND LOGO rediesign for a surgical medical practice located in Australia.
LOGO - should have an upper limb, shoulder, joint or convey movement
General feel is business/professional. Layout should allow as much space for text as possible
Include the information that is on the proof below that is the current letter head
Need designs in .dotx template and .pdf

Target Market(s)

general practitioner doctors

Industry/Entity Type

medical

Font styles to use
Sans Serif

Colors
0054AA
0677BA
7BADD7
CADEEF
E8F1F8

```html
<!DOCTYPE html>
<html lang="en">
<head>
<meta charset="utf-8">
<title>Ashgrove Orthopaedics – Stationery</title>
<link rel="stylesheet" href="https://fonts.googleapis.com/css2?family=Rubik:wght@300;400;500;700&display=swap">
<style>
  :root{
    --navy:#1e1650;
    --red:#e8262f;
    --gold:#c8902c;
    --ink:#2b2b3a;
    --paper:#ffffff;
    --banner-top:#f4f4f5;
    --banner-bottom:#c9cacd;
    --stage:#3a3c3f;
    --desk:#5b5b5b;
  }
  *{box-sizing:border-box;margin:0;padding:0}
  html,body{width:1200px;height:2277px;overflow:hidden}
  body{font-family:"Rubik",sans-serif;color:var(--ink);background:var(--desk);position:relative}

  .brand-banner{position:absolute;left:0;top:0;width:1200px;height:143px;
    background:linear-gradient(180deg,var(--banner-top),var(--banner-bottom));
    display:flex;align-items:center;justify-content:center}

  .logotype{display:flex;align-items:center;gap:14px;font-family:"Rubik",sans-serif;font-weight:300;color:var(--navy)}
  .logotype__square{width:34px;height:34px;background:var(--red);flex:none}
  .logotype__words{display:flex;flex-direction:column;line-height:1}
  .logotype__name{font-size:30px;letter-spacing:5px}
  .logotype__sub{font-size:13px;letter-spacing:6.4px;margin-top:5px}
  .logotype--light{color:#ffffff}

  .card-stage{position:absolute;left:0;top:143px;width:1200px;height:914px;background:var(--stage);
    display:flex;align-items:center;justify-content:center;gap:50px}
  .card{width:520px;height:300px;position:relative;box-shadow:0 14px 30px rgba(0,0,0,.45)}
  .card--front{background:var(--paper)}
  .card--back{background:var(--navy);display:flex;align-items:center;justify-content:center}
  .card--front .logotype{position:absolute;left:30px;top:34px}
  .card__person{position:absolute;right:30px;top:36px;text-align:right}
  .card__name{font-size:17px;font-weight:500;color:var(--gold);letter-spacing:.3px}
  .card__name strong{color:var(--red);font-weight:700}
  .card__role{font-size:11px;color:var(--navy);margin-top:3px;padding-bottom:3px;border-bottom:1.5px solid var(--navy);display:inline-block}
  .card__contacts{position:absolute;left:30px;top:150px;list-style:none;font-size:10.5px;color:#55566a}
  .card__contacts li{display:flex;align-items:flex-start;gap:8px;margin-bottom:8px;line-height:1.3}
  .card__contacts svg{width:13px;height:13px;flex:none}

  .letterhead{position:absolute;left:231px;top:1160px;width:738px;height:1015px;background:var(--paper);
    box-shadow:0 18px 40px rgba(0,0,0,.35)}
  .letterhead .logotype{position:absolute;left:24px;top:40px}
  .letterhead__author{position:absolute;right:0;top:36px;text-align:left;width:370px}
  .letterhead__name{font-size:23px;font-weight:700;color:var(--gold)}
  .letterhead__role{display:flex;align-items:center;gap:6px;font-size:14px;color:var(--navy);margin-top:5px}
  .letterhead__role::after{content:"";flex:1;height:1.5px;background:var(--navy)}
  .letterhead__address{position:absolute;left:24px;top:908px;display:flex;align-items:center;gap:8px;font-size:13.5px;color:#5a5a66}
  .letterhead__band{position:absolute;left:0;top:936px;width:738px;height:30px;background:var(--red);
    display:flex;align-items:center;gap:22px;padding-left:24px;color:#fff;font-size:14px}
  .letterhead__band span{display:flex;align-items:center;gap:8px}
  .letterhead__note{position:absolute;left:26px;top:976px;font-size:12.5px;font-weight:500;color:var(--navy)}
  .icon-box{width:18px;height:18px;flex:none}
</style>
</head>
<body>

<svg width="0" height="0" style="position:absolute">
  <defs>
    <symbol id="i-pin" viewBox="0 0 16 16"><rect width="16" height="16" rx="2" fill="currentColor"/><path d="M8 3a3.3 3.3 0 0 0-3.3 3.3C4.7 9 8 13 8 13s3.3-4 3.3-6.7A3.3 3.3 0 0 0 8 3zm0 4.6a1.3 1.3 0 1 1 0-2.6 1.3 1.3 0 0 1 0 2.6z" fill="#fff"/></symbol>
    <symbol id="i-phone" viewBox="0 0 16 16"><rect width="16" height="16" rx="2" fill="currentColor"/><path d="M5.2 3.2l1.6 2.2-1 1.1c.6 1.4 1.6 2.4 3 3l1.1-1 2.2 1.6-.8 1.9C7.6 12 4 8.4 3.3 4z" fill="#fff"/></symbol>
    <symbol id="i-fax" viewBox="0 0 16 16"><rect width="16" height="16" rx="2" fill="currentColor"/><path d="M5 3h6v3H5zM3.5 6.5h9v5h-2v-2h-5v2h-2zM5.5 10h5v3h-5z" fill="#fff"/></symbol>
    <symbol id="i-mail" viewBox="0 0 16 16"><rect width="16" height="16" rx="2" fill="currentColor"/><path d="M3 4.5h10v7H3zM3 4.5l5 4 5-4" fill="none" stroke="#fff" stroke-width="1.2"/></symbol>
    <symbol id="i-web" viewBox="0 0 16 16"><rect width="16" height="16" rx="2" fill="currentColor"/><path d="M5 3.5l6 5.2-2.6.3 1.5 3-1.2.6-1.5-3L5 11.5z" fill="#fff"/></symbol>
  </defs>
</svg>

<header class="brand-banner">
  <div class="logotype">
    <span class="logotype__square"></span>
    <span class="logotype__words"><span class="logotype__name">ASHGROVE</span><span class="logotype__sub">ORTHOPAEDICS</span></span>
  </div>
</header>

<section class="card-stage">
  <article class="card card--front">
    <div class="logotype">
      <span class="logotype__square" style="width:24px;height:24px"></span>
      <span class="logotype__words"><span class="logotype__name" style="font-size:22px;letter-spacing:3.5px">ASHGROVE</span><span class="logotype__sub" style="font-size:9.5px;letter-spacing:4.6px">ORTHOPAEDICS</span></span>
    </div>
    <div class="card__person">
      <p class="card__name">MARTIN J. <strong>COLLIER</strong></p>
      <p class="card__role">Managing Director</p>
    </div>
    <ul class="card__contacts">
      <li style="color:#55566a"><svg style="color:var(--red)"><use href="#i-pin"/></svg><span>Suite 4, Level 2 Northbank<br>Private Hospital, Ashgrove Vic 3061</span></li>
      <li><svg style="color:var(--navy)"><use href="#i-phone"/></svg><span>94170325</span></li>
      <li><svg style="color:var(--navy)"><use href="#i-fax"/></svg><span>85502147</span></li>
      <li><svg style="color:var(--navy)"><use href="#i-mail"/></svg><span>info@danhartwell.com.au</span></li>
      <li><svg style="color:var(--navy)"><use href="#i-web"/></svg><span>danhartwell.com.au</span></li>
    </ul>
  </article>

  <article class="card card--back">
    <div class="logotype logotype--light">
      <span class="logotype__square"></span>
      <span class="logotype__words"><span class="logotype__name">ASHGROVE</span><span class="logotype__sub">ORTHOPAEDICS</span></span>
    </div>
  </article>
</section>

<article class="letterhead">
  <div class="logotype">
    <span class="logotype__square"></span>
    <span class="logotype__words"><span class="logotype__name">ASHGROVE</span><span class="logotype__sub">ORTHOPAEDICS</span></span>
  </div>
  <div class="letterhead__author">
    <p class="letterhead__name">Daniel Hartwell MBBS FRACS</p>
    <p class="letterhead__role">Orthopaedic Surgeon 408215KT</p>
  </div>

  <p class="letterhead__address"><svg class="icon-box" style="color:var(--gold)"><use href="#i-pin"/></svg>Suite 4, Level 2 Northbank Private Hospital, Ashgrove Vic 3061</p>
  <div class="letterhead__band">
    <span><svg class="icon-box" style="color:var(--navy)"><use href="#i-phone"/></svg>94170325</span>
    <span><svg class="icon-box" style="color:var(--navy)"><use href="#i-fax"/></svg>85502147</span>
    <span><svg class="icon-box" style="color:var(--navy)"><use href="#i-mail"/></svg>info@danhartwell.com.au</span>
  </div>
  <p class="letterhead__note">We accept Medlink communication</p>
</article>

</body>
</html>
```